Brightpath Mentoring Brochure

Looking for a tri-fold brochure that can work as a self-mailer and a leave behind piece.

Brightpath Mentoring works with parents and young teens to develop personal capacity; emotional intelligence, resilience, communications skills, goal setting, and a high level of consciousness and attitude control. See our website at www.brightpathmentoring.example.

Cover should be provocative... quote about 46% of entering freshman from the website is powerful

We are talking about a 11"x8.5" opened, 3.7 x 8.5 folded tri-fold... there should be plenty of content on our website... The inside panels could be as follows

left panel could be a graphic and part of "the Story" Head line about 46% of entering freshman taking more than 6 years to get a degree.

Middle and right panels could be the three programs... Attitudinal Assessment, Group coaching on Communication, Value based S.M.A.R.T. goal setting and defeating internal blocks. and One on One Family coaching.

Target Market(s)

Parents and teens in the 9th grade age range

Industry/Entity Type

Communications

Requirements
Must have
• Provocative Title
"Did you know 46% of entering college freshman fail to receive a degree within 6 years?"
Powerful graphics to communicate transformation from anger and conflict between parents and teens to collaboration and cooperation.

```html
<!DOCTYPE html>
<html lang="en">
<head>
<meta charset="utf-8">
<title>Brightpath Mentoring Brochure</title>
<link href="https://fonts.googleapis.com/css2?family=Arimo:wght@400;700&display=swap" rel="stylesheet">
<style>
  :root {
    --bg: #e4e4e0;
    --paper: #ffffff;
    --wave-deep: #2f5f8f;
    --wave-mid: #3d72a4;
    --wave-light: #5a8fbf;
    --navy: #1f3f73;
    --crimson: #a3202a;
    --maroon: #8a1c2a;
    --body: #3a3a3a;
    --photo-top: #dfe3e8;
    --photo-bottom: #c46a86;
  }
  * { box-sizing: border-box; margin: 0; padding: 0; }
  html, body { width: 1200px; height: 806px; overflow: hidden; }
  body {
    background: var(--bg);
    font-family: "Arimo", Arial, sans-serif;
    position: relative;
  }
  .panel {
    position: absolute;
    background: var(--paper);
    overflow: hidden;
    box-shadow: 0 2px 6px rgba(0,0,0,.15);
  }
  .panel-cover { left: 80px; top: 100px; width: 360px; height: 590px; }
  .panel-back  { left: 790px; top: 118px; width: 290px; height: 540px; }
  .wave { position: absolute; left: 0; width: 100%; display: block; }
  .wave-top { top: 0; }
  .wave-bottom { bottom: 0; }

  .brand {
    position: absolute; top: 78px; left: 0; width: 100%;
    text-align: center;
  }
  .brand-mark {
    width: 40px; height: 40px; border-radius: 50%;
    border: 2px solid var(--maroon);
    margin: 0 auto 6px;
  }
  .brand-name {
    font-size: 19px; font-weight: 400; color: #222; letter-spacing: .2px;
  }
  .brand-rule {
    width: 120px; height: 1px; background: var(--maroon); margin: 3px auto 2px;
  }
  .brand-tagline { font-size: 5px; color: #444; font-style: italic; }

  .headline {
    position: absolute; top: 180px; left: 0; width: 100%;
    text-align: center; font-weight: 700; font-size: 17px; line-height: 1.05;
    transform: scaleX(.92);
  }
  .headline .lead { color: var(--crimson); }
  .headline .tail { color: var(--navy); }

  .cover-photo {
    position: absolute; left: 50px; top: 225px; width: 300px; height: 300px;
    background: linear-gradient(180deg, var(--photo-top), #b9a79a 45%, var(--photo-bottom));
    border-radius: 4px 4px 0 0;
  }

  .back-content { position: absolute; top: 118px; left: 28px; right: 24px; }
  .section-title { font-size: 12px; font-weight: 700; color: var(--navy); margin-bottom: 8px; }
  .about-text {
    font-size: 8.6px; line-height: 1.45; color: var(--body); text-align: justify;
    margin-bottom: 10px;
  }
  .contact { position: absolute; top: 372px; left: 80px; right: 14px; }
  .contact-title { font-size: 11px; color: var(--maroon); margin-bottom: 3px; }
  .contact-line { font-size: 9.2px; color: #222; line-height: 1.4; }
  .contact-line b { font-weight: 700; }
</style>
</head>
<body>

<section class="panel panel-cover">
  <svg class="wave wave-top" viewBox="0 0 360 95" height="95" preserveAspectRatio="none" aria-hidden="true">
    <path d="M0 0H360V45C250 35 120 60 0 95Z" fill="var(--wave-deep)"/>
    <path d="M0 0H360V30C250 25 120 45 0 78Z" fill="var(--wave-mid)"/>
    <path d="M0 0H360V18C240 10 110 28 0 55Z" fill="var(--wave-light)"/>
  </svg>

  <div class="brand">
    <div class="brand-mark"></div>
    <div class="brand-name">Brightpath Mentoring</div>
    <div class="brand-rule"></div>
    <div class="brand-tagline">"Helping Families Grow Stronger Through Guided Mentoring Every Day"</div>
  </div>

  <h1 class="headline">
    <span class="lead">46% of college freshmen fail</span><br>
    <span class="tail">to get a degree within 6 years</span>
  </h1>

  <div class="cover-photo" role="img" aria-label="Photo of a frustrated teenage girl with arms crossed, her father and mother standing behind her with hands on hips"></div>

  <svg class="wave wave-bottom" viewBox="0 0 360 70" height="70" preserveAspectRatio="none" aria-hidden="true">
    <path d="M0 10C120 0 250 20 360 5V70H0Z" fill="var(--wave-mid)"/>
    <path d="M0 30C120 18 250 35 360 22V70H0Z" fill="var(--wave-deep)"/>
  </svg>
</section>

<section class="panel panel-back">
  <svg class="wave wave-top" viewBox="0 0 290 70" height="70" preserveAspectRatio="none" aria-hidden="true">
    <path d="M0 0H290V70C190 50 90 48 0 62Z" fill="var(--wave-deep)"/>
    <path d="M0 0H290V45C190 30 90 30 0 40Z" fill="var(--wave-mid)"/>
    <path d="M40 0C120 10 220 20 290 40V0Z" fill="var(--wave-light)" opacity=".6"/>
  </svg>

  <div class="back-content">
    <h2 class="section-title">About Us</h2>
    <p class="about-text">Kelvin is an experienced "C" suite executive with a 30-year track record of developing strategic plans, transforming complex businesses and building revenues and profits in the information and media industries. Over the course of his career he has recruited, hired, trained and developed hundreds of talented individuals ranging from entry level to senior executives.</p>
    <p class="about-text">In 2011, Kelvin took a year off to attend the Northfield Institute for Coaching Practice where he earned his Certification as a Professional Coach. In late 2011 he established Keystone Advisory Coaching, a firm providing coaching and advisory services to business executives facing a wide range of issues from mild distress to significant dysfunction. The practice focuses on organizations requiring significant change..</p>
  </div>

  <div class="contact">
    <h3 class="contact-title">CONTACT US</h3>
    <p class="contact-line">218 Maplecrest Lane Suite 40-B</p>
    <p class="contact-line">Fairbrook, VA 20999</p>
    <p class="contact-line"><b>Phone:</b> (555) 014-7012</p>
    <p class="contact-line"><b>Email:</b> kelvinrt4success@example.com</p>
  </div>

  <svg class="wave wave-bottom" viewBox="0 0 290 90" height="90" preserveAspectRatio="none" aria-hidden="true">
    <path d="M0 8C100 -2 200 0 290 12V90H0Z" fill="var(--wave-deep)"/>
    <path d="M0 30C100 20 200 22 290 30V90H0Z" fill="var(--wave-mid)"/>
    <path d="M0 60C100 50 200 55 290 48V90H0Z" fill="var(--wave-light)" opacity=".7"/>
  </svg>
</section>

</body>
</html>
```